Horse Rehabilitation & Boarding Facility is looking for a new website - Design & Code

We are looking to freshen up the look of our existing website using a new color scheme and logo. Looking for something visually grabbing and vibrant. We would like to see a website that displays trust, dedication and passion. Needs to be responsive and mobile friendly for all browsers and coded for both Android & IOS. SEO is also important.

See website content document for full details and page layout.

Coding

Coded - Design and coding required

Number of Pages Required

5+ page

Font styles to use
Sans Serif

Requirements
Must have
• Needs to be responsive and mobile friendly for all browsers and coded for both Android & IOS. SEO is also important.

new color scheme and logo

Focus on Rehab and Boarding Services. No reference to racing.

Use only photos with horses standing.
Nice to have
• Main picture should be the drone looking east over track
Should not have
• Do not reference World Class Facility. No pictures of horses running.

No newsletter sign up.

No news feed.

```html
<!DOCTYPE html>
<html lang="en">
<head>
<meta charset="utf-8">
<title>Larkfield Equine – Training & Rehab Centre</title>
<link rel="stylesheet" href="https://fonts.googleapis.com/css2?family=Source+Sans+3:wght@300;400;600;700&display=swap">
<style>
:root{
  --red:#b01f2e;
  --gold:#c8a84a;
  --ink:#2b2b2b;
  --muted:#6f6f6f;
  --light-band:#f3f1f2;
  --grey-band:#e9e7e8;
  --footer:#4b4a4c;
  --frame:#7a7a7a;
  --white:#ffffff;
}
*{margin:0;padding:0;box-sizing:border-box}
html,body{width:1200px;height:3595px;overflow:hidden;background:var(--white)}
body{position:relative;font-family:"Source Sans 3",Arial,sans-serif;color:var(--ink)}
.abs{position:absolute}

/* top strip */
.top-strip{left:0;top:0;width:1200px;height:11px;background:var(--red);z-index:3}

/* hero */
.hero{left:0;top:0;width:1200px;height:659px;overflow:hidden}
.hero-aerial{left:0;top:0;width:1200px;height:659px;
  background:linear-gradient(160deg,#4d5f3f 0%,#3d4d33 35%,#56664a 55%,#33412b 100%)}
.hero-shade{left:0;top:0;width:1200px;height:659px;background:rgba(0,0,0,.28)}
.hero-portrait{left:865px;top:125px;width:335px;height:534px;
  background:linear-gradient(180deg,#a06a42 0%,#d9c39a 45%,#5a4a5c 100%)}
.brand-badge{left:103px;top:11px;width:173px;height:195px;z-index:2}
.brand-badge svg{position:absolute;left:0;top:0}
.brand-name{position:absolute;left:0;top:62px;width:173px;text-align:center;
  font-size:28px;line-height:32px;font-weight:400;color:var(--red)}
.main-nav{left:717px;top:67px;height:25px;display:flex;align-items:center;z-index:2}
.main-nav a{font-size:15.5px;color:var(--white);text-decoration:none;margin-right:27px;line-height:25px}
.main-nav a.active{background:var(--red);padding:0 17px;font-weight:700;border-radius:2px;margin-right:21px}
.hero-title{left:106px;top:306px;font-size:53px;line-height:47px;color:var(--white);font-weight:400;letter-spacing:.5px}

/* intro */
.intro-title{left:0;top:722px;width:1200px;text-align:center;font-size:42px;line-height:36px;color:var(--red);font-weight:400}
.intro-sub{left:0;top:800px;width:1200px;text-align:center;font-size:22px;font-weight:300;color:var(--muted)}
.intro-photo{left:254px;top:857px;width:633px;height:219px;border:1px solid #333;
  background:linear-gradient(180deg,#d8dde2 0%,#e9eaea 45%,#9a8b6a 75%,#7c8c52 100%)}
.intro-text{left:202px;top:1112px;width:705px;text-align:center;font-size:13.5px;line-height:17.5px;color:#444}
.btn-join{left:506px;top:1221px;width:129px;height:39px;background:var(--red);color:var(--white);
  font-weight:700;font-size:14px;line-height:39px;text-align:center}

/* service bands */
.band-light{left:0;top:1347px;width:1200px;height:641px;background:var(--light-band)}
.band-grey{left:0;top:2648px;width:1200px;height:642px;background:var(--grey-band)}
.section-title{font-size:43px;line-height:44px;color:var(--red);font-weight:400;white-space:nowrap}
.section-sub{font-size:20px;line-height:24px;font-weight:300;color:var(--muted)}
.accent-rule{height:2px;background:var(--red)}
.lead{font-size:14px;line-height:24px;color:var(--ink)}
.body-copy{font-size:13px;line-height:24px;color:var(--muted);font-weight:400}
.btn-learn{background:var(--red);color:var(--white);font-size:12px;letter-spacing:1.5px;text-align:center;font-weight:600;border-radius:3px}
.btn-learn.square{border-radius:0;letter-spacing:0;font-weight:700;font-size:13px}
.framed{border:8px solid var(--frame);background:var(--white);padding:7px}
.framed .photo{width:100%;height:100%}

/* footer */
.footer{left:0;top:3290px;width:1200px;height:262px;background:var(--footer)}
.footer-brand{left:121px;top:3400px;width:176px;text-align:center;font-size:32px;line-height:34px;color:var(--white)}
.footer-head{font-weight:700;font-size:16px;color:var(--gold);text-decoration:underline;letter-spacing:.3px}
.footer-text{font-size:13.5px;line-height:18.5px;color:var(--white)}
.quick-links{list-style:none}
.quick-links li{height:25.5px;font-size:13.5px;line-height:18px;color:var(--white);display:flex;align-items:center}
.quick-links li svg{margin-right:9px}
.copyright{left:0;top:3552px;width:1200px;height:43px;background:var(--red);color:var(--white);font-size:13px;line-height:43px;text-align:center}
</style>
</head>
<body>

<div class="abs top-strip"></div>

<header class="abs hero">
  <div class="abs hero-aerial" role="img" aria-label="Aerial drone view of the training track, paddocks and red barns"></div>
  <div class="abs hero-shade"></div>
  <div class="abs hero-portrait" role="img" aria-label="Blonde woman embracing a chestnut horse with a white blaze"></div>
  <div class="abs brand-badge">
    <svg width="173" height="195" viewBox="0 0 173 195"><polygon points="0,0 173,0 173,165 86.5,195 0,165" fill="#fff"/></svg>
    <div class="brand-name">Larkfield<br>Equine</div>
  </div>
  <nav class="abs main-nav">
    <a class="active" href="#">Home</a>
    <a href="#">About us</a>
    <a href="#">Facility</a>
    <a href="#">Our Services</a>
    <a href="#">Contact</a>
  </nav>
  <h1 class="abs hero-title">PREMIUM CARE FOR<br>THE HEALTH &amp; FITNESS<br>OF YOUR HORSE</h1>
</header>

<section>
  <h2 class="abs intro-title">PREMIUM CARE FOR<br>THE HEALTH &amp; FITNESS OF YOUR HORSE</h2>
  <p class="abs intro-sub">Welcome to Training &amp; Rehab center</p>
  <div class="abs intro-photo" role="img" aria-label="Chestnut horse standing in a white-fenced paddock beside red barns"></div>
  <p class="abs intro-text">The Larkfield Equine Training &amp; rehab center feature both Conditioning &amp; rehab services for all breeds of horses under one roof! With over 200 years of combined hands-on experience, they understand the importance of maintaining health, well being and peak performance of the beautiful animals whether for pleasure riding, competition or everyday trail work</p>
  <div class="abs btn-join">JOIN US NOW</div>
</section>

<section>
  <div class="abs band-light"></div>
  <h2 class="abs section-title" style="left:133px;top:1424px">REHABILITATION</h2>
  <p class="abs section-sub" style="left:136px;top:1470px">We love and respect our horses</p>
  <div class="abs accent-rule" style="left:137px;top:1511px;width:67px"></div>
  <p class="abs lead" style="left:137px;top:1533px;width:418px">As a horse owner, trainer or veterinarian, you know how challenging it is to transport horses to different facilities to receive the care they need. Now the Larkfield Centre, located just 13 km (8 miles) north of Birchvale, Alberta, offers a full service, safe and cost effective alternative for the rehab and/or training of your horse.</p>
  <p class="abs body-copy" style="left:137px;top:1670px;width:390px">If rehabilitation for an injury or health issue is required, Larkfield can maintain your horse's fitness level with a carefully supervised exercise program while they go through rehab. Also our state of the art equipment helps speed up the recovery time needed to get your horse quickly back to health and well being. The result is a shorter rehabilitation time saving you time and money.</p>
  <div class="abs btn-learn" style="left:137px;top:1839px;width:128px;height:43px;line-height:43px">LEARN MORE</div>
  <div class="abs framed" style="left:614px;top:1427px;width:396px;height:468px">
    <div class="photo" role="img" aria-label="Woman in a maroon polo shirt standing beside a dark bay horse" style="background:linear-gradient(160deg,#dfe6e8 0%,#3a2a22 40%,#6e1e30 80%,#7a2438 100%)"></div>
  </div>
</section>

<section>
  <div class="abs framed" style="left:138px;top:2087px;width:395px;height:466px">
    <div class="photo" role="img" aria-label="Handler leading a dark horse out of its stall in the boarding barn" style="background:linear-gradient(170deg,#c9c3bb 0%,#3b2e28 45%,#6e2a35 80%,#b8bcc0 100%)"></div>
  </div>
  <h2 class="abs section-title" style="left:661px;top:2100px">BOARDING</h2>
  <p class="abs section-sub" style="left:664px;top:2145px">The Larkfield Centre Features<br>the best for &nbsp;your Horse</p>
  <p class="abs lead" style="left:664px;top:2245px;width:400px">Our team understand the importance of maintaining health, well being and peak performance of the beautiful animals whether for Pleasure riding, competition or quiet retirement.</p>
  <p class="abs body-copy" style="left:668px;top:2337px;width:390px">Horse boarding is like rental housing for your horse. ... A horse can be housed in a barn with other horses and receive the care they need. Owners can visit their horse for riding, grooming, training, etc. Horse boarding services may vary based on the company and the price.</p>
  <div class="abs btn-learn" style="left:665px;top:2486px;width:128px;height:42px;line-height:42px">LEARN MORE</div>
</section>

<section>
  <div class="abs band-grey"></div>
  <h2 class="abs section-title" style="left:170px;top:2738px">DEDICATED &nbsp;TEAM</h2>
  <p class="abs section-sub" style="left:173px;top:2784px">Management And Operations Tteam</p>
  <div class="abs accent-rule" style="left:176px;top:2833px;width:65px"></div>
  <p class="abs lead" style="left:174px;top:2870px;width:415px">With over 200 years of combined hands-on experience, they understand the importance of maintaining health, well being and peak performance of the beautiful animals whether for pleasure riding, competition or quiet retirement</p>
  <p class="abs body-copy" style="left:174px;top:2988px;width:385px">Has worked all their lives with horses, particularly high-end performance and sport horses. They combine effectively managing the day to day operations &nbsp;of the Equine Centre with their expertise in rehab and special care of horses recovering from injuries</p>
  <div class="abs btn-learn square" style="left:180px;top:3137px;width:127px;height:37px;line-height:37px">LEARN MORE</div>
  <div class="abs" role="img" aria-label="Team member standing with a bay horse in front of a red barn wall" style="left:661px;top:2724px;width:397px;height:470px;background:linear-gradient(150deg,#e8734f 0%,#d0493a 40%,#5a2a24 70%,#b33a36 100%)"></div>
</section>

<footer>
  <div class="abs footer"></div>
  <div class="abs footer-brand">Larkfield<br>Equine</div>

  <h3 class="abs footer-head" style="left:410px;top:3340px">ABOUT US</h3>
  <p class="abs footer-text" style="left:410px;top:3386px;width:192px;text-align:justify">The Larkfield management team is compromised of people who live, eat and breath horses and that passion is what makes the Centre so unique.</p>
  <p class="abs footer-text" style="left:410px;top:3490px">Read More &gt;&gt;</p>

  <h3 class="abs footer-head" style="left:709px;top:3340px">QUICK LINKS</h3>
  <ul class="abs quick-links" style="left:714px;top:3383px">
    <li><svg width="7" height="9" viewBox="0 0 7 9"><polygon points="0,0 7,4.5 0,9" fill="#c8a84a"/></svg>Home</li>
    <li><svg width="7" height="9" viewBox="0 0 7 9"><polygon points="0,0 7,4.5 0,9" fill="#c8a84a"/></svg>About us</li>
    <li><svg width="7" height="9" viewBox="0 0 7 9"><polygon points="0,0 7,4.5 0,9" fill="#c8a84a"/></svg>Our service</li>
    <li><svg width="7" height="9" viewBox="0 0 7 9"><polygon points="0,0 7,4.5 0,9" fill="#c8a84a"/></svg>Feciliity</li>
    <li><svg width="7" height="9" viewBox="0 0 7 9"><polygon points="0,0 7,4.5 0,9" fill="#c8a84a"/></svg>Contact Us</li>
  </ul>

  <h3 class="abs footer-head" style="left:921px;top:3340px">CONTACT US</h3>
  <p class="abs footer-text" style="left:921px;top:3386px">Birchvale, Alberta, Canada<br>40210 - RR 108,<br>PO Box 4402, X0X 1A1</p>
  <p class="abs footer-text" style="left:921px;top:3460px">PH: 555-014-2218<br>Cell: 555-014-2290<br>info@larkfieldequine.example</p>

  <div class="abs copyright">Copyright © 2021 Larkfield Equine training &amp; Rehab centre</div>
</footer>

</body>
</html>
```